Banner ad Design

Project:
Creation of online advertising banners for use on Brixel AdPlume network and for display advertising on one product on our website.
http://brightparcel.com.au/computers/ebook/7inch-velmora-3g-mini-tablet-netbook-colour-ebook-reader.html
Headline to appear on all banners:
Hot!!! 3G Velmora tablet Only $159 (with our website logo )
Formats
- 728 x 90
- 468 x 60
- 300 x 250
- 160 x 600
- 120 x 600
- 336 x 280
Note: Would prefer to have banners ASAP (sooner than 5 days if possible). Designers who act on it quickly, and supply great designs will most likely be awarded the winner
Advertising

```html
<!DOCTYPE html>
<html lang="en">
<head>
<meta charset="utf-8">
<title>Bright Parcel – Velmora Tablet Banners</title>
<link rel="stylesheet" href="https://fonts.googleapis.com/css2?family=Archivo+Black&display=swap">
<style>
  :root {
    --canvas: #ffffff;
    --frame: #1a1a1a;
    --orange-light: #f4a06a;
    --orange: #ec8247;
    --orange-deep: #d9652a;
    --logo-green: #3e9a3a;
    --logo-square: #f08a4b;
    --white: #ffffff;
    --gold-top: #fff4b8;
    --gold-mid: #e8c04a;
    --gold-low: #a8791c;
    --shadow: rgba(90, 35, 5, 0.55);
    --device-dark: #2a2a2a;
    --device-light: #8a8f96;
    --badge: #1c1c1c;
    --badge-face: #f2f2f2;
  }
  * { box-sizing: border-box; margin: 0; padding: 0; }
  html, body {
    width: 1200px; height: 900px; overflow: hidden;
    background: var(--canvas);
    font-family: "Archivo Black", "Arial Black", sans-serif;
  }
  .canvas { position: relative; width: 1200px; height: 900px; }

  .banner {
    position: absolute; top: 16px; height: 868px;
    border: 2px solid var(--frame);
    overflow: hidden;
    background: radial-gradient(ellipse at 50% 40%, var(--orange-light) 0%, var(--orange) 55%, var(--orange-deep) 100%);
  }
  .banner--wide { left: 336px; width: 240px; }
  .banner--narrow { left: 714px; width: 178px; }

  .logo-band { position: absolute; left: 0; top: 0; width: 100%; }
  .logo-band svg { display: block; width: 100%; }
  .brand {
    position: absolute; left: 0; right: 0;
    display: flex; align-items: center; justify-content: center; gap: 8px;
    color: var(--logo-green); line-height: 1;
  }
  .brand__square { background: var(--logo-square); flex: none; }
  .banner--wide .brand { top: 30px; font-size: 25px; }
  .banner--wide .brand__square { width: 28px; height: 28px; }
  .banner--narrow .brand { top: 24px; font-size: 18px; gap: 6px; }
  .banner--narrow .brand__square { width: 20px; height: 20px; }

  .offer {
    position: absolute; left: 0; right: 0;
    text-align: center; line-height: 0.98;
    color: var(--white);
    text-shadow: 2px 3px 3px var(--shadow);
  }
  .offer span { display: block; }
  .offer .gold {
    background: linear-gradient(180deg, var(--gold-top) 0%, var(--gold-mid) 50%, var(--gold-low) 100%);
    -webkit-background-clip: text; background-clip: text;
    color: transparent;
    text-shadow: none;
    filter: drop-shadow(2px 3px 2px var(--shadow));
  }
  .banner--wide .offer { top: 170px; font-size: 40px; }
  .banner--wide .offer .hot { font-size: 58px; letter-spacing: -1px; }
  .banner--wide .offer .price { font-size: 58px; }
  .banner--narrow .offer { font-size: 29px; }
  .banner--narrow .offer .hot { font-size: 38px; letter-spacing: -1px; }
  .banner--narrow .offer .price { font-size: 38px; }
  .banner--narrow .offer--top { top: 116px; }
  .banner--narrow .offer--bottom { top: 646px; }

  .tablet-photo {
    position: absolute;
    background: linear-gradient(150deg, var(--device-light) 0%, #dfe2e6 30%, #cfd3d8 60%, var(--device-dark) 100%);
    border-radius: 26px 0 0 26px;
  }
  .banner--wide .tablet-photo { left: 0; top: 478px; width: 240px; height: 370px; }
  .banner--narrow .tablet-photo { left: 0; top: 350px; width: 178px; height: 280px; border-radius: 20px 0 0 20px; }

  .badge {
    position: absolute; background: var(--badge); border-radius: 6px;
    display: flex; align-items: center; justify-content: flex-end; padding-right: 4px;
  }
  .badge__face { background: var(--badge-face); border-radius: 3px; }
  .banner--wide .badge { right: 10px; bottom: 14px; width: 56px; height: 28px; }
  .banner--wide .badge__face { width: 22px; height: 20px; }
  .banner--narrow .badge { right: 8px; top: 604px; width: 46px; height: 24px; }
  .banner--narrow .badge__face { width: 18px; height: 16px; }
</style>
</head>
<body>
<main class="canvas">

  <section class="banner banner--wide" aria-label="160 by 600 banner">
    <div class="logo-band">
      <svg viewBox="0 0 240 110" preserveAspectRatio="none" aria-hidden="true">
        <path d="M0 0 H240 V86 Q120 122 0 92 Z" fill="#ffffff"/>
        <path d="M0 92 Q120 122 240 86 V94 Q120 128 0 98 Z" fill="#c9c9c9"/>
      </svg>
    </div>
    <div class="brand"><span class="brand__name">Bright Parcel</span><span class="brand__square"></span></div>

    <h2 class="offer">
      <span class="gold hot">HOT!!!</span>
      <span>3G</span>
      <span>Velmora</span>
      <span>Tablet</span>
      <span>ONLY</span>
      <span class="gold price">$159</span>
    </h2>

    <div class="tablet-photo" role="img" aria-label="Photo of a black tablet showing a newspaper website"></div>
    <div class="badge" aria-hidden="true"><span class="badge__face"></span></div>
  </section>

  <section class="banner banner--narrow" aria-label="120 by 600 banner">
    <div class="logo-band">
      <svg viewBox="0 0 178 90" preserveAspectRatio="none" aria-hidden="true">
        <path d="M0 0 H178 V68 Q89 100 0 74 Z" fill="#ffffff"/>
        <path d="M0 74 Q89 100 178 68 V75 Q89 106 0 80 Z" fill="#c9c9c9"/>
      </svg>
    </div>
    <div class="brand"><span class="brand__name">Bright Parcel</span><span class="brand__square"></span></div>

    <h2 class="offer offer--top">
      <span class="gold hot">HOT!!!</span>
      <span>3G</span>
      <span>Velmora</span>
      <span>Tablet</span>
      <span>ONLY</span>
      <span class="gold price">$159</span>
    </h2>

    <div class="tablet-photo" role="img" aria-label="Photo of a black tablet showing a newspaper website"></div>
    <div class="badge" aria-hidden="true"><span class="badge__face"></span></div>

    <h2 class="offer offer--bottom">
      <span class="gold hot">HOT!!!</span>
      <span>3G</span>
      <span>Velmora</span>
      <span>Tablet</span>
      <span>ONLY</span>
      <span class="gold price">$159</span>
    </h2>
  </section>

</main>
</body>
</html>
```